Packaging for a new tea company

Hi guys we need a new packaging design for a tea company we are starting

Our competitors are leafara, zo ren tea

I have uploaded pictures of our competitors for you to see the sample
The label need to be catchy

Our brand is called #PlumVexaTea
We need two packaging designs one for Day Tea and one for calmora

Detox - slim - cleanse

Also needs to says 14 Day Orvalin

Target Market(s)

Young people

Industry/Entity Type

It Company

Colors
000000

Requirements
Must have
• #plumvexatea
Nice to have
• Herbal tea supplement 50gram
• Max label size 13.5cm x 16.5 cm
• Personally I like the paper brown bag as it looks like a higher quality and as the label is a sticker I think this would make the product look a lot better
Should not have
• Nothing

```html
<!DOCTYPE html>
<html lang="en">
<head>
<meta charset="utf-8">
<title>PlumVexaTea Pouches</title>
<link rel="stylesheet" href="https://fonts.googleapis.com/css2?family=Patrick+Hand+SC&family=Herr+Von+Muellerhoff&display=swap">
<style>
  :root {
    --backdrop: #cbc4bd;
    --kraft: #c99b6b;
    --kraft-dark: #b5855a;
    --kraft-light: #d6ab7d;
    --ink: #111111;
    --paper: #ecebea;
    --olive: #a3ad1f;
    --white: #f4f4f2;
  }
  html, body {
    margin: 0;
    padding: 0;
    width: 1200px;
    height: 873px;
    overflow: hidden;
    background: var(--backdrop);
  }
  .stage {
    position: relative;
    width: 1200px;
    height: 873px;
  }
  .pouch {
    position: absolute;
    top: 100px;
    width: 446px;
    height: 656px;
  }
  .pouch--calmora { left: 120px; }
  .pouch--solara { left: 656px; }
  .pouch__bag {
    position: absolute;
    inset: 0;
    width: 100%;
    height: 100%;
  }
  .label {
    position: absolute;
    left: 99px;
    top: 220px;
    width: 250px;
    height: 272px;
    border-radius: 50%;
    font-family: "Patrick Hand SC", cursive;
  }
  .label--dark { background: var(--ink); color: var(--white); }
  .label--light { background: var(--paper); color: var(--ink); }
  .label > * {
    position: absolute;
    left: 0;
    right: 0;
    margin: 0;
    text-align: center;
    line-height: 1;
    white-space: nowrap;
  }
  .label__mark {
    left: 115px;
    right: auto;
    top: 24px;
    width: 20px;
    height: 20px;
    border-radius: 50%;
    background: var(--olive);
  }
  .label__brand {
    top: 52px;
    font-size: 28px;
    color: var(--olive);
    letter-spacing: 0.5px;
  }
  .label__script {
    top: 86px;
    font-family: "Herr Von Muellerhoff", cursive;
    font-size: 70px;
  }
  .label__type {
    top: 148px;
    font-size: 38px;
  }
  .label__program {
    top: 184px;
    font-size: 32px;
    color: var(--olive);
  }
  .label__weight {
    top: 236px;
    font-size: 20px;
  }
  .pouch__variant {
    position: absolute;
    left: 0;
    right: 0;
    top: 508px;
    margin: 0;
    text-align: center;
    font-family: "Patrick Hand SC", cursive;
    font-size: 21px;
    line-height: 1;
    color: var(--ink);
  }
</style>
</head>
<body>
<main class="stage">

  <section class="pouch pouch--calmora">
    <svg class="pouch__bag" viewBox="0 0 446 656" aria-hidden="true">
      <path d="M0 0 H446 V150 Q446 450 420 640 Q223 662 26 640 Q0 450 0 150 Z" fill="var(--kraft)"/>
      <path d="M0 0 H446 V8 H0 Z" fill="var(--kraft-light)"/>
      <line x1="6" y1="48" x2="440" y2="48" stroke="var(--kraft-dark)" stroke-width="2"/>
      <line x1="6" y1="74" x2="440" y2="74" stroke="var(--kraft-light)" stroke-width="2"/>
    </svg>
    <div class="label label--dark">
      <span class="label__mark"></span>
      <p class="label__brand">PLUMVEXATEA</p>
      <p class="label__script">Herbal Tea</p>
      <p class="label__type">SUPPLEMENT</p>
      <p class="label__program">14 DAY ORVALIN</p>
      <p class="label__weight">50 GRAM</p>
    </div>
    <p class="pouch__variant">CALMORA</p>
  </section>

  <section class="pouch pouch--solara">
    <svg class="pouch__bag" viewBox="0 0 446 656" aria-hidden="true">
      <path d="M0 0 H446 V150 Q446 450 420 640 Q223 662 26 640 Q0 450 0 150 Z" fill="var(--kraft)"/>
      <path d="M0 0 H446 V8 H0 Z" fill="var(--kraft-light)"/>
      <line x1="6" y1="48" x2="440" y2="48" stroke="var(--kraft-dark)" stroke-width="2"/>
      <line x1="6" y1="74" x2="440" y2="74" stroke="var(--kraft-light)" stroke-width="2"/>
    </svg>
    <div class="label label--light">
      <span class="label__mark"></span>
      <p class="label__brand">PLUMVEXATEA</p>
      <p class="label__script">Herbal Tea</p>
      <p class="label__type">SUPPLEMENT</p>
      <p class="label__program">14 DAY ORVALIN</p>
      <p class="label__weight">50 GRAM</p>
    </div>
    <p class="pouch__variant">SOLARA</p>
  </section>

</main>
</body>
</html>
```